Wordpress website design for a high-end painting business

We are currently rebranding and are looking to update our Wordpress theme. We have recently rebranded our logo on PixelHarbor, and would like our website to be equally as refined.
Our business is named “Kestrel Painters”. We are a high-end painting business that is known for being professional and having high standards. Our clean and professional image is important as it separates us from our competition. Our current website can be found at www.wrenfieldcoatings.co.nz . We designed the site ourselves so it is understandably rudimentary. We are generally happy with the. page layout of our existing site, but we like a professional remodel. Any ideas on improvement welcomed.
We would like the front page of the website to summarise all of the info throughout the whole website (I.e introduction, photos, testimonials, contact info etc.) as visitors typically scroll through the first page to see that we are reputable and get to our contact number/email contact at the bottom of the page. We would like this first page to give a clean well rounded image of our business. We would like the gallery to be a scroll through of large photos, as it is difficult to see paint details in smaller photos. A contact page with an enquiry section would also be good.
For the colour scheme, we would like something that fits a bold, masculine and high end theme (similar to our logo attached).
We would like the footer to include Veltora paint logos and the accredited painter logo we have included as these are important to our profession.
We have attached some photos of our work also. I will add more in the coming days. More can also be found on our website.
If you have questions or comments, please don’t hesitate to ask and I will get back as soon as possible.
We are open to your own interpretation or ideas for a better layout/site provided they fit the general brief of being a well rounded site for our profession.
Thanks,
Kestrel Painters.
Target Market(s)
High end clients
Industry/Entity Type
Painting (interior and exterior)
Coding
Coded - Design and coding required
Requirements
Must have
- Classy feel, separating us from typical painting companies. Well rounded homepage.
Nice to have
- Lots of examples of our work
Should not have
- Untidy paint motifs (eg, paint droplets, paint splashes)

```html
<!DOCTYPE html>
<html lang="en">
<head>
<meta charset="utf-8">
<title>Kestrel Painters</title>
<link href="https://fonts.googleapis.com/css2?family=Tinos:wght@400;700&family=Roboto:wght@300;400;500;700&display=swap" rel="stylesheet">
<style>
:root{
  --tan:#8a6a4b;
  --ink:#1c1d21;
  --text:#555a60;
  --darker:#15171a;
  --paper:#ffffff;
  --mist:#f1f1f1;
  --line:#dcdcdc;
}
*{box-sizing:border-box;margin:0;padding:0}
html,body{width:1200px;height:5344px;overflow:hidden}
body{font-family:"Roboto",Arial,sans-serif;color:var(--text);background:var(--paper);position:relative}
.serif{font-family:"Tinos","Times New Roman",serif}
.btn{position:absolute;background:var(--tan);color:#fff;font-size:15px;font-weight:500;border-radius:22px;display:flex;align-items:center;justify-content:center;gap:8px}
.btn-dot{width:14px;height:14px;border-radius:50%;background:#fff;display:inline-flex;align-items:center;justify-content:center}
.btn-dot svg{width:8px;height:8px}

/* header */
.site-header{position:absolute;left:0;top:0;width:1200px;height:120px;background:#fff}
.brand{position:absolute;left:100px;top:18px;display:flex;flex-direction:column;align-items:center;gap:6px}
.brand-mark{width:60px;height:60px;border-radius:50%;background:var(--ink)}
.brand-name{font-family:"Tinos",serif;font-weight:700;font-size:14px;color:var(--ink);letter-spacing:1px}
.main-nav{position:absolute;left:385px;top:76px;display:flex;gap:40px;font-size:16px;font-weight:500;color:var(--ink)}
.main-nav .active{color:var(--tan)}
.top-contact{position:absolute;top:14px;display:flex;gap:10px;align-items:center}
.top-contact .ic{width:36px;height:36px;border-radius:50%;background:var(--ink);display:flex;align-items:center;justify-content:center}
.top-contact small{display:block;font-size:11px;color:#777}
.top-contact b{display:block;font-size:15px;color:var(--ink);font-weight:500}

/* hero */
.hero{position:absolute;left:0;top:120px;width:1200px;height:640px;background:linear-gradient(180deg,#4f83c4 0%,#8fb4de 38%,#7c8591 60%,#4f5a4a 82%,#6f8a4f 100%)}
.hero h1{position:absolute;left:0;width:1200px;top:108px;text-align:center;color:#fff;font-size:46px;letter-spacing:1px}
.hero p{position:absolute;left:370px;width:460px;top:180px;text-align:center;color:#fff;font-size:16px;line-height:1.4}
.hero .arrow{position:absolute;top:280px;color:#fff;font-size:30px}

/* section headings */
.sec-title{position:absolute;left:0;width:1200px;text-align:center;font-family:"Tinos",serif;font-weight:700;font-size:44px;color:var(--ink)}

/* services */
.service{position:absolute;width:320px;height:320px;border-radius:6px;overflow:hidden}
.service-label{position:absolute;left:0;bottom:22px;width:100%;text-align:center;color:#fff;font-family:"Tinos",serif;font-weight:700;font-size:28px;line-height:1.05}

/* about */
.about{position:absolute;left:0;top:1700px;width:1200px;height:540px;background:var(--mist)}
.about-photo{position:absolute;left:140px;top:80px;width:300px;height:300px;border-radius:50%;background:radial-gradient(circle at 50% 30%,#9fc1e3 0%,#d8c9a8 45%,#7a8a56 85%);border:8px solid #fff;box-shadow:0 0 0 3px #2b2b2b}
.about h2{position:absolute;left:652px;top:72px;font-size:44px;color:var(--ink)}
.about p{position:absolute;left:652px;width:450px;font-size:13px;line-height:1.75;color:#666}

/* testimonials */
.reviews{position:absolute;left:0;top:2240px;width:1200px;height:640px;background:linear-gradient(180deg,#2e3239,#1f2227)}
.reviews h2{position:absolute;left:0;width:1200px;top:160px;text-align:center;color:#fff;font-size:40px}
.review{position:absolute;top:250px;width:320px;height:260px;border:2px solid #cfcfcf;border-radius:4px;padding:20px 18px;color:#e6e6e6}
.review .q{font-family:"Tinos",serif;font-size:44px;line-height:30px;color:#fff;font-weight:700}
.review p{font-size:13px;line-height:1.6;margin-top:10px}
.stars{color:#e2a23a;font-size:16px;letter-spacing:2px;margin-top:8px}
.review-name{position:absolute;top:522px;width:320px;text-align:center;color:#fff;font-family:"Tinos",serif;font-weight:700;font-size:18px}
.review-date{position:absolute;top:546px;width:320px;text-align:center;color:#bbb;font-size:10px}
.rev-arrow{position:absolute;top:360px;width:44px;height:44px;background:#e8e8e8;border-radius:4px;display:flex;align-items:center;justify-content:center}

/* gallery */
.shot{position:absolute;width:488px;height:372px;border-radius:4px;overflow:hidden}
.shot-cap{position:absolute;left:26px;bottom:26px;color:#fff;font-size:18px;font-weight:500}

/* quote */
.quote{position:absolute;left:0;top:4088px;width:1200px;height:632px;background:#f3f3f3}
.quote-art{position:absolute;left:0;top:0;width:640px;height:632px;background:linear-gradient(90deg,#d9a84e 0%,#e8c27a 40%,#efe7d9 75%,#f3f3f3 100%)}
.quote h2{position:absolute;left:656px;top:70px;font-size:44px;color:var(--ink)}
.field{position:absolute;left:652px;width:448px;height:48px;background:#fff;border:1px solid var(--line);border-radius:4px;font-size:13px;color:#777;padding:14px 16px}

/* footer */
.site-footer{position:absolute;left:0;top:4720px;width:1200px;height:624px;background:var(--darker);color:#ddd}
.f-contact{position:absolute;top:50px;display:flex;gap:14px;align-items:center}
.f-contact .ic{width:46px;height:46px;border-radius:50%;border:2px solid #777;display:flex;align-items:center;justify-content:center}
.f-contact span{font-size:15px;line-height:1.4;color:#fff}
.f-rule{position:absolute;left:100px;top:200px;width:1000px;height:1px;background:#3a3d42}
.f-col{position:absolute;top:268px}
.f-col h4{font-size:15px;color:#fff;font-weight:700;margin-bottom:14px;letter-spacing:.3px}
.f-col li{list-style:none;font-size:13px;line-height:26px;color:#cfcfcf}
.f-col p{font-size:12px;line-height:1.6;color:#bbb}
.social li{display:flex;align-items:center;gap:10px}
.social i{width:22px;height:22px;border-radius:50%;background:#3a3e45;display:inline-block}
.copyright{position:absolute;left:0;top:580px;width:1200px;text-align:center;font-size:13px;color:#bbb}
</style>
</head>
<body>

<header class="site-header">
  <div class="brand">
    <div class="brand-mark"></div>
    <div class="brand-name">KESTREL PAINTERS</div>
  </div>
  <nav class="main-nav">
    <span class="active">HOME</span><span>SERVICES</span><span>GALLERY</span><span>ABOUT</span><span>TESTIMONIALS</span><span>CONTACT</span>
  </nav>
  <div class="top-contact" style="left:655px">
    <div class="ic"><svg width="18" height="14" viewBox="0 0 18 14"><rect x="1" y="1" width="16" height="12" fill="none" stroke="#fff" stroke-width="1.6"/><path d="M1 1l8 7 8-7" fill="none" stroke="#fff" stroke-width="1.6"/></svg></div>
    <div><small>Get in Touch</small><b>hello@kestrelpainters.co.nz</b></div>
  </div>
  <div class="top-contact" style="left:960px">
    <div class="ic"><svg width="16" height="16" viewBox="0 0 24 24"><path d="M6.6 10.8c1.4 2.8 3.8 5.1 6.6 6.6l2.2-2.2c.3-.3.7-.4 1-.2 1.1.4 2.3.6 3.6.6.6 0 1 .4 1 1V20c0 .6-.4 1-1 1C10.6 21 3 13.4 3 4c0-.6.4-1 1-1h3.5c.6 0 1 .4 1 1 0 1.3.2 2.5.6 3.6.1.3 0 .7-.2 1z" fill="#fff"/></svg></div>
    <div><small>Call Us Today</small><b>021 555 0142</b></div>
  </div>
</header>

<section class="hero" role="img" aria-label="Photo of a modern grey and white painted house under a blue sky">
  <h1 class="serif">KESTREL PAINTERS</h1>
  <p>Lorem ipsum dolor sit amet, consectetur adipiscing elit, sed do eiusmod tempor incididunt Lorem ipsum dolor sit amet, consectetur</p>
  <div class="btn" style="left:495px;top:265px;width:210px;height:44px">Schedule a Service <span class="btn-dot"><svg viewBox="0 0 8 8"><path d="M2 1l3 3-3 3" fill="none" stroke="#8a6a4b" stroke-width="1.6"/></svg></span></div>
  <span class="arrow" style="left:58px">&#8249;</span>
  <span class="arrow" style="left:1128px">&#8250;</span>
</section>

<h2 class="sec-title" style="top:855px">Our Services</h2>
<div class="service" style="left:100px;top:944px;background:linear-gradient(180deg,#8fb7e0,#b9b3a4 55%,#4f6b3c)" role="img" aria-label="Photo of a freshly painted house exterior"><div class="service-label">Exterior Painting</div></div>
<div class="service" style="left:440px;top:944px;background:linear-gradient(180deg,#e6dfd3,#b8a48c 60%,#6b5640)" role="img" aria-label="Photo of a painted interior room"><div class="service-label">Interior Painting</div></div>
<div class="service" style="left:780px;top:944px;background:linear-gradient(90deg,#c9c5bd,#7e8a88 55%,#d7d3cc)" role="img" aria-label="Photo of a patterned wallpapered wall"><div class="service-label">Wallpapering</div></div>
<div class="service" style="left:100px;top:1284px;background:linear-gradient(160deg,#e8e8e8,#c2a58a 55%,#6c5f55)" role="img" aria-label="Photo of a hand holding a plastering trowel"><div class="service-label">Plastering</div></div>
<div class="service" style="left:440px;top:1284px;background:linear-gradient(180deg,#7fa9d8,#a46a52 55%,#4a6a3a)" role="img" aria-label="Photo of a house being cleaned"><div class="service-label">Waterblasting &amp;<br>House Cleaning</div></div>
<div class="service" style="left:780px;top:1284px;background:linear-gradient(180deg,#a8c0dc,#5e656e 55%,#3a3d42)" role="img" aria-label="Photo of a painted roof"><div class="service-label">Roof Painting</div></div>

<section class="about">
  <div class="about-photo" role="img" aria-label="Photo of a two storey painted villa"></div>
  <h2 class="serif">About Us</h2>
  <p style="top:140px">Here at Kestrel Painters, we take a lot of pride in our work. We strive to ensure the highest quality paint work, paying close attention to detail to provide a long lasting finish. Our clients are always our priority, and we aim to deliver beyond their expectations. It is our goal to provide an excellent service from start to finish through clear communication, fine quality and transparency with our pricing.</p>
  <p style="top:290px">We take great pride in the preparation of surfaces for painting and only use the best quality products to ensure we achieve the best finish for you. Our qualified interior designer can also assist you with your colour selection as part of our free colour consultancy service.</p>
  <div class="btn" style="left:652px;top:470px;width:172px;height:46px">Learn More <span class="btn-dot"><svg viewBox="0 0 8 8"><path d="M2 1l3 3-3 3" fill="none" stroke="#8a6a4b" stroke-width="1.6"/></svg></span></div>
</section>

<section class="reviews">
  <h2 class="serif">What Our Customer Say</h2>
  <div class="rev-arrow" style="left:30px"><svg width="14" height="14" viewBox="0 0 14 14"><path d="M9 2L4 7l5 5" fill="none" stroke="#222" stroke-width="2"/></svg></div>
  <div class="rev-arrow" style="left:1126px"><svg width="14" height="14" viewBox="0 0 14 14"><path d="M5 2l5 5-5 5" fill="none" stroke="#222" stroke-width="2"/></svg></div>

  <div class="review" style="left:100px"><div class="q">&ldquo;</div><p>We chose the team to complete painting work around our home. They are very knowledgeable, careful and thorough. We felt we could trust them to do an excellent job in a timely manner. Their prices are reasonable and communication throughout has been excellent.</p><div class="stars">★★★★★</div></div>
  <div class="review-name" style="left:100px">HELENA</div><div class="review-date" style="left:100px">JUNE 2018</div>

  <div class="review" style="left:440px"><div class="q">&ldquo;</div><p>We chose the team to complete painting work around our home. They are very knowledgeable, careful and thorough. We felt we could trust them to do an excellent job in a timely manner. Their prices are reasonable and communication throughout has been excellent.</p><div class="stars">★★★★★</div></div>
  <div class="review-name" style="left:440px">HELENA</div><div class="review-date" style="left:440px">JUNE 2018</div>

  <div class="review" style="left:780px"><div class="q">&ldquo;</div><p>We chose the team to complete painting work around our home. They are very knowledgeable, careful and thorough. We felt we could trust them to do an excellent job in a timely manner. Their prices are reasonable and communication throughout has been excellent.</p><div class="stars">★★★★★</div></div>
  <div class="review-name" style="left:780px">HELENA</div><div class="review-date" style="left:780px">JUNE 2018</div>
</section>

<h2 class="sec-title" style="top:3036px">Our Gallery</h2>
<div class="shot" style="left:100px;top:3124px;background:linear-gradient(180deg,#9fc0e2,#dcdcd8 50%,#5f7f45)" role="img" aria-label="Photo of a repainted white weatherboard house"><div class="shot-cap">Exterior repaint in Te Kauwhata, Waikato.</div></div>
<div class="shot" style="left:612px;top:3124px;background:linear-gradient(180deg,#5b8fd0,#6e7486 50%,#4f6a3f)" role="img" aria-label="Photo of a repainted grey house with white trim"><div class="shot-cap">Exterior repaint in Te Kauwhata, Waikato.</div></div>
<div class="shot" style="left:100px;top:3520px;background:linear-gradient(180deg,#f2f0ec,#d6d1c8 55%,#5c4f45)" role="img" aria-label="Photo of a repainted white home office"><div class="shot-cap">Home office repaint, Hamilton.</div></div>
<div class="shot" style="left:612px;top:3520px;background:linear-gradient(180deg,#ecebe7,#c9c6c0 55%,#2f3e5a)" role="img" aria-label="Photo of a repainted living room"><div class="shot-cap">Exterior repaint in Enderly, Hamilton.</div></div>
<div class="btn" style="left:511px;top:3940px;width:178px;height:46px">View More <span class="btn-dot"><svg viewBox="0 0 8 8"><path d="M2 1l3 3-3 3" fill="none" stroke="#8a6a4b" stroke-width="1.6"/></svg></span></div>

<section class="quote">
  <div class="quote-art" role="img" aria-label="Painter in white overalls rolling paint onto a wall"></div>
  <h2 class="serif">Get Your Free Quote</h2>
  <div class="field" style="top:158px">First Name</div>
  <div class="field" style="top:222px">Last Name</div>
  <div class="field" style="top:286px">Email</div>
  <div class="field" style="top:350px">Phone Number</div>
  <div class="field" style="top:414px;height:100px">Message</div>
  <div class="btn" style="left:930px;top:530px;width:170px;height:46px">Submit Now <span class="btn-dot"><svg viewBox="0 0 8 8"><path d="M2 1l3 3-3 3" fill="none" stroke="#8a6a4b" stroke-width="1.6"/></svg></span></div>
</section>

<footer class="site-footer">
  <div class="f-contact" style="left:100px">
    <div class="ic"><svg width="16" height="20" viewBox="0 0 16 20"><path d="M8 1a6 6 0 0 0-6 6c0 4.5 6 12 6 12s6-7.5 6-12a6 6 0 0 0-6-6z" fill="#fff"/><circle cx="8" cy="7" r="2.2" fill="#15171a"/></svg></div>
    <span>Location:<br>Kestrel Painters And Decorators</span>
  </div>
  <div class="f-contact" style="left:490px">
    <div class="ic"><svg width="16" height="16" viewBox="0 0 24 24"><path d="M6.6 10.8c1.4 2.8 3.8 5.1 6.6 6.6l2.2-2.2c.3-.3.7-.4 1-.2 1.1.4 2.3.6 3.6.6.6 0 1 .4 1 1V20c0 .6-.4 1-1 1C10.6 21 3 13.4 3 4c0-.6.4-1 1-1h3.5c.6 0 1 .4 1 1 0 1.3.2 2.5.6 3.6.1.3 0 .7-.2 1z" fill="#fff"/></svg></div>
    <span>Phone:<br>021 555 0142</span>
  </div>
  <div class="f-contact" style="left:810px">
    <div class="ic"><svg width="18" height="14" viewBox="0 0 18 14"><rect x="1" y="1" width="16" height="12" fill="none" stroke="#fff" stroke-width="1.6"/><path d="M1 1l8 7 8-7" fill="none" stroke="#fff" stroke-width="1.6"/></svg></div>
    <span>Email:<br>hello@kestrelpainters.co.nz</span>
  </div>
  <div class="f-rule"></div>

  <div class="f-col" style="left:100px">
    <h4>QUICK LINKS</h4>
    <ul><li>Home</li><li>Services</li><li>Gallery</li><li>About</li><li>Testimonials</li><li>Contact</li></ul>
  </div>
  <div class="f-col" style="left:280px;width:300px">
    <h4>SIGN UP TO RECEIVE EMAIL</h4>
    <p>Sed ut perspiciatis unde omnis iste natus error sit voluptatem accusantium</p>
    <div style="margin-top:18px;width:280px;height:40px;border-radius:20px;background:#fff;color:#777;font-size:12px;padding:12px 18px">Enter Email</div>
    <div class="btn" style="position:relative;margin-top:14px;left:120px;width:164px;height:42px">Submit Now <span class="btn-dot"><svg viewBox="0 0 8 8"><path d="M2 1l3 3-3 3" fill="none" stroke="#8a6a4b" stroke-width="1.6"/></svg></span></div>
  </div>
  <div class="f-col social" style="left:635px">
    <h4>FOLLOW US</h4>
    <ul><li><i></i>Circlefeed</li><li><i></i>Chirper</li><li><i></i>ProNetwork</li><li><i></i>Photoloft</li></ul>
  </div>
  <div class="f-col" style="left:820px;width:280px">
    <div style="width:170px;height:120px;background:#2f5fae;border-radius:4px" role="img" aria-label="Accredited painter badge"></div>
    <p style="margin-top:10px">Sed ut perspiciatis unde omnis iste natus error sit voluptatem accusantium doloremque, totam rem aperiam, eaque ipsa</p>
  </div>
  <div class="copyright">&copy;Copyright@2022 kestreldecorators All Rights Reserved.</div>
</footer>

</body>
</html>
```